Velmoro Crafts

I would like to have a more comprehensive e-commerce website.

Please use my current website as reference and its content: https://velmorocrafts.com/.

Please code the website. I'd like to have e-commerce functionalities.

```html
<!DOCTYPE html>
<html lang="en">
<head>
<meta charset="utf-8">
<title>Velmoro Crafts — Handcrafted Candles</title>
<link rel="stylesheet" href="https://fonts.googleapis.com/css2?family=Young+Serif&family=Poppins:wght@400;500;600;700&display=swap">
<style>
:root{
  --navy:#0d2b3b;
  --teal:#79bec4;
  --coral:#f04b4f;
  --ink:#1d2b38;
  --muted:#4a5663;
  --line:#d7e4e6;
  --white:#ffffff;
  --serif:"Young Serif", Georgia, serif;
  --sans:"Poppins", Arial, sans-serif;
}
*{box-sizing:border-box;margin:0;padding:0}
html,body{width:1200px;height:3745px;overflow:hidden;background:var(--white)}
body{font-family:var(--sans);color:var(--ink);position:relative}
.abs{position:absolute}
a{color:inherit;text-decoration:none}
.btn{position:absolute;display:flex;align-items:center;justify-content:center;background:var(--coral);color:var(--white);font:600 12.5px var(--sans);text-transform:uppercase;border-radius:26px;letter-spacing:.2px}
.photo{position:absolute}

/* top bar + header */
.topbar{left:0;top:0;width:1200px;height:36px;background:var(--navy);color:var(--white);font:500 11px var(--sans);display:flex;align-items:center;justify-content:center}
.brand{left:87px;top:46px;height:72px;display:flex;align-items:center;gap:12px}
.brand-dot{width:54px;height:54px;border-radius:50%;background:var(--coral)}
.brand-name{font:700 21px var(--sans);color:var(--navy);text-transform:uppercase;letter-spacing:.5px}
.nav{top:74px;font:500 12.5px var(--sans);text-transform:uppercase;color:var(--ink)}
.nav.active{color:var(--coral)}
.icon{top:66px}
.cart-label{left:1059px;top:65px;font:600 12px var(--sans);color:var(--navy);line-height:1.1}
.cart-label small{display:block;font:400 11px var(--sans);color:var(--muted)}

/* hero */
.hero-left{left:0;top:128px;width:381px;height:632px;background:linear-gradient(160deg,#d9d6d0,#b7b1a6 60%,#a08c6e)}
.hero-mid{left:381px;top:128px;width:436px;height:632px;background:var(--teal)}
.hero-right{left:817px;top:128px;width:383px;height:632px;background:linear-gradient(170deg,#8f8a7c,#5f6b45 35%,#cfcdc8 60%,#8f6d5b)}
.hero-kicker{left:381px;top:262px;width:436px;text-align:center;font:400 19px var(--serif);color:var(--white)}
.hero-title{left:381px;top:300px;width:436px;text-align:center;font:400 46px/45px var(--serif);color:var(--white)}
.hero-copy{left:430px;top:457px;width:340px;text-align:center;font:400 12.5px/19px var(--sans);color:var(--white)}
.hero-dots{left:522px;top:712px;display:flex;gap:0}
.hero-dots span{width:50px;height:3px;background:var(--white)}
.hero-dots span.on{background:var(--navy)}

/* discover */
.disc-a{left:67px;top:864px;width:326px;height:377px;border-radius:0 0 163px 163px;background:linear-gradient(170deg,#d5d0c8,#b8ad9e 55%,#ead9c6)}
.disc-b{left:889px;top:839px;width:170px;height:208px;border-radius:85px 85px 0 0;background:radial-gradient(circle at 50% 38%,#e98a9a,#8fc3d8 30%,#e8e6e2 55%,#cfcac3)}
.disc-c{left:1003px;top:982px;width:145px;height:145px;border-radius:50%;background:radial-gradient(circle,#ffffff,#ecebe6 60%,rgba(255,255,255,0))}
.disc-d{left:870px;top:1174px;width:169px;height:132px;border-radius:0 0 80px 0;background:linear-gradient(160deg,#8b7f6e,#7c8b5a 40%,#c9c4bb 70%,#836d5c)}
.disc-title{left:240px;top:970px;width:720px;text-align:center;font:400 40px/49px var(--serif);color:var(--navy)}

/* products */
.prod-panel{left:0;top:1382px;width:599px;height:636px;background:var(--teal)}
.prod-photo{left:599px;top:1382px;width:601px;height:636px;background:linear-gradient(175deg,#b6a293,#9c9183 35%,#8a7f73 70%,#6d625a)}
.prod-title{left:0;top:1465px;width:599px;text-align:center;font:400 44px var(--serif);color:var(--white)}
.tab{top:1553px;font:600 10.5px var(--sans);color:var(--white);text-transform:uppercase}
.tab.on{color:var(--coral);text-decoration:underline;text-underline-offset:3px}
.arrow{width:40px;height:40px;border-radius:50%;background:var(--white);display:flex;align-items:center;justify-content:center;top:1696px}
.prod-card{left:199px;top:1616px;width:200px;height:199px;border:3px solid var(--white);border-radius:10px;background:linear-gradient(160deg,#d6d3cd,#a9a39a 60%,#c7bfb2)}
.prod-name{left:0;top:1830px;width:599px;text-align:center;font:400 30px var(--serif);color:var(--white)}

/* about */
.about-arch{left:215px;top:2087px;width:384px;height:437px;border-radius:192px 192px 0 0;background:linear-gradient(180deg,#c89b6b,#9c6a3f 45%,#6a4327 80%,#3d2a1d)}
.about-small{left:89px;top:2432px;width:230px;height:183px;border-radius:0 0 90px 0;border:2px solid var(--white);background:linear-gradient(160deg,#cfcbc4,#a59f96 55%,#b68a64)}
.about-title{left:684px;top:2124px;width:420px;font:400 45px/53px var(--serif);color:var(--navy)}
.about-copy{left:684px;top:2250px;width:380px;font:400 12.3px/19.6px var(--sans);color:var(--muted)}

/* testimonials */
.testi-title{left:0;top:2656px;width:1200px;text-align:center;font:400 45px var(--serif);color:var(--navy)}
.card{top:2752px;width:485px;height:198px;border:1px solid #9fd0d4;border-radius:100px;padding:28px 0 0 86px}
.stars{display:flex;gap:2px;margin-bottom:12px}
.quote{width:360px;font:400 14px/20.5px var(--sans);color:var(--muted)}
.who{margin-top:12px;font:700 14px var(--sans);color:var(--ink)}
.tdots{left:576px;top:2999px;display:flex;gap:10px}
.tdots span{width:9px;height:9px;border-radius:50%;background:#b9c6cc}
.tdots span.on{background:var(--navy)}

/* connect */
.connect{left:0;top:3079px;width:1200px;height:267px;background:var(--teal)}
.connect-title{left:89px;top:3143px;font:400 45px var(--serif);color:var(--white)}
.connect-copy{left:89px;top:3216px;width:560px;font:400 15.5px/26px var(--sans);color:var(--white)}

/* footer */
.foot-brand{left:145px;top:3500px;display:flex;align-items:center;gap:12px}
.foot-head{top:3443px;font:400 24px var(--serif);color:var(--navy)}
.foot-link{font:400 12.5px var(--sans);color:var(--muted)}
.contact-row{left:822px;display:flex;align-items:center;gap:10px;font:400 12.5px var(--sans);color:var(--muted)}
.social{top:3567px;width:41px;height:41px;border:1px solid var(--navy);border-radius:50%;display:flex;align-items:center;justify-content:center}
.social i{width:10px;height:10px;border-radius:50%;background:var(--navy)}
.rule{left:89px;top:3690px;width:1022px;height:1px;background:#cfd7db}
.copyright{left:0;top:3710px;width:1200px;text-align:center;font:400 12px var(--sans);color:var(--muted)}
.totop{left:1132px;top:3670px;width:40px;height:40px;border-radius:50%;background:var(--navy);display:flex;align-items:center;justify-content:center}
</style>
</head>
<body>

<header>
  <div class="abs topbar">FREE SHIPPING on Orders Over $50 | Orders Typically Processed in 1-2 Business Days</div>
  <a class="abs brand" href="#"><span class="brand-dot"></span><span class="brand-name">Velmoro Crafts</span></a>
  <nav>
    <a class="abs nav active" style="left:554px" href="#">Home</a>
    <a class="abs nav" style="left:618px" href="#">About Us</a>
    <a class="abs nav" style="left:704px" href="#">Products</a>
    <a class="abs nav" style="left:797px" href="#">Contact Us</a>
  </nav>
  <svg class="abs icon" style="left:912px" width="28" height="30" viewBox="0 0 28 30" fill="none" stroke="#0d2b3b" stroke-width="2"><circle cx="14" cy="9" r="6"/><path d="M3 28c1-7 6-10 11-10s10 3 11 10z"/></svg>
  <svg class="abs icon" style="left:963px" width="30" height="28" viewBox="0 0 30 28" fill="none" stroke="#0d2b3b" stroke-width="2"><path d="M15 26S2 18 2 9a6.5 6.5 0 0 1 13-2 6.5 6.5 0 0 1 13 2c0 9-13 17-13 17z"/></svg>
  <svg class="abs icon" style="left:1014px;top:62px" width="40" height="36" viewBox="0 0 40 36" fill="none" stroke="#0d2b3b" stroke-width="2"><path d="M2 8h5l4 17h17l4-12H9"/><circle cx="13" cy="31" r="2"/><circle cx="26" cy="31" r="2"/><circle cx="31" cy="7" r="6" fill="#f04b4f" stroke="none"/><text x="31" y="10" font-size="8" fill="#fff" stroke="none" text-anchor="middle" font-family="Poppins, sans-serif">0</text></svg>
  <div class="abs cart-label">MY CART<small>Items</small></div>
</header>

<section class="hero">
  <div class="photo hero-left" role="img" aria-label="Concrete candle with twine and a handmade with love tag"></div>
  <div class="abs hero-mid"></div>
  <div class="photo hero-right" role="img" aria-label="Ribbed white concrete candle outdoors beside plants"></div>
  <p class="abs hero-kicker">Welcome to Velmoro Crafts!</p>
  <h1 class="abs hero-title">Handcrafted Candles Inspired by the Southwest</h1>
  <p class="abs hero-copy">We are a family-owned business passionate about creating beautiful</p>
  <a class="btn" style="left:479px;top:520px;width:241px;height:48px" href="#">Our Handcrafted Candles</a>
  <div class="abs hero-dots"><span></span><span class="on"></span><span></span></div>
</section>

<section class="discover">
  <div class="photo disc-a" role="img" aria-label="Hexagonal candle with a thank you card"></div>
  <div class="photo disc-b" role="img" aria-label="Candle topped with colourful beads"></div>
  <div class="photo disc-c" role="img" aria-label="White gardenia flower"></div>
  <div class="photo disc-d" role="img" aria-label="Textured concrete planter with a small plant"></div>
  <h2 class="abs disc-title">Discover the First scent in our base notes collection simple, grounding scents to calm candles</h2>
  <a class="btn" style="left:509px;top:1153px;width:181px;height:49px" href="#">View Categories</a>
</section>

<section class="products">
  <div class="abs prod-panel"></div>
  <div class="photo prod-photo" role="img" aria-label="White concrete planter with succulents and sand"></div>
  <h2 class="abs prod-title">Our Products</h2>
  <a class="abs tab on" style="left:68px" href="#">Sola Collection</a>
  <a class="abs tab" style="left:182px" href="#">Mesa Collection</a>
  <a class="abs tab" style="left:308px" href="#">New Collection</a>
  <a class="abs tab" style="left:432px" href="#">Ridge Collection</a>
  <a class="abs arrow" style="left:61px" href="#" aria-label="Previous"><svg width="10" height="10" viewBox="0 0 10 10"><path d="M6 2 3 5l3 3" fill="none" stroke="#0d2b3b" stroke-width="1.5"/></svg></a>
  <a class="abs arrow" style="left:496px" href="#" aria-label="Next"><svg width="10" height="10" viewBox="0 0 10 10"><path d="M4 2l3 3-3 3" fill="none" stroke="#0d2b3b" stroke-width="1.5"/></svg></a>
  <div class="abs prod-card" role="img" aria-label="Sola Collection concrete candle with tag"></div>
  <p class="abs prod-name">Sola Collection - $7</p>
  <a class="btn" style="left:189px;top:1897px;width:220px;height:46px" href="#">Buy Our Sola Collection</a>
</section>

<section class="about">
  <div class="photo about-arch" role="img" aria-label="Lit candle in a textured copper-toned vessel"></div>
  <div class="photo about-small" role="img" aria-label="Three diamond-pattern candles with tags"></div>
  <h2 class="abs about-title">About Velmoro Crafts</h2>
  <p class="abs about-copy">Velmoro Crafts is a Hispanic woman-owned business that began with a simple dream. Co-founder Marisol Quintero, captivated by the art of crafting, started creating candles as gifts for loved ones. Inspired to minimize waste, Marisol envisioned eco-friendly containers that could be repurposed after the candle burned. This passion project took root in her backyard, where she designed and crafted the very first Velmoro candles.</p>
  <a class="btn" style="left:685px;top:2429px;width:135px;height:47px" href="#">Read More</a>
</section>

<section class="testimonials">
  <h2 class="abs testi-title">Client’s Testimonials</h2>
  <article class="abs card" style="left:89px">
    <div class="stars"><svg width="90" height="16" viewBox="0 0 90 16" fill="#f4a53a"><g id="star"><path d="M8 1l2 5h5l-4 3 2 5-5-3-5 3 2-5-4-3h5z"/></g><use href="#star" x="18"/><use href="#star" x="36"/><use href="#star" x="54"/><use href="#star" x="72"/></svg></div>
    <p class="quote">“I adore their candles! They create such a peaceful ambiance in my home, and I love that I’m supporting a good cause with each purchase.”</p>
    <p class="who">— Clara R.</p>
  </article>
  <article class="abs card" style="left:596px">
    <div class="stars"><svg width="90" height="16" viewBox="0 0 90 16" fill="#f4a53a"><use href="#star"/><use href="#star" x="18"/><use href="#star" x="36"/><use href="#star" x="54"/><use href="#star" x="72"/></svg></div>
    <p class="quote">“I adore their candles! They create such a peaceful ambiance in my home, and I love that I’m supporting a good cause with each purchase.”</p>
    <p class="who">— Denise T.</p>
  </article>
  <article class="abs card" style="left:1105px"></article>
  <div class="abs tdots"><span></span><span class="on"></span><span></span></div>
</section>

<section class="connect-wrap">
  <div class="abs connect"></div>
  <h2 class="abs connect-title">Let's Connect With Us!</h2>
  <p class="abs connect-copy">We would love to hear from you! Have questions about our candles or want to learn more about Velmoro Crafts?</p>
  <a class="btn" style="left:862px;top:3190px;width:229px;height:47px" href="#">Get In Touch With Us</a>
</section>

<footer>
  <a class="abs foot-brand" href="#"><span class="brand-dot"></span><span class="brand-name">Velmoro Crafts</span></a>
  <h3 class="abs foot-head" style="left:488px">Company</h3>
  <a class="abs foot-link" style="left:489px;top:3494px" href="#">Shop</a>
  <a class="abs foot-link" style="left:489px;top:3526px" href="#">About Us</a>
  <a class="abs foot-link" style="left:489px;top:3557px" href="#">Products</a>
  <a class="abs foot-link" style="left:489px;top:3589px" href="#">Contact</a>
  <h3 class="abs foot-head" style="left:655px">Products</h3>
  <a class="abs foot-link" style="left:656px;top:3494px" href="#">Sola Collection</a>
  <a class="abs foot-link" style="left:656px;top:3526px" href="#">Mesa Collection</a>
  <a class="abs foot-link" style="left:656px;top:3557px" href="#">New Collection</a>
  <a class="abs foot-link" style="left:656px;top:3589px" href="#">Ridge Collection</a>
  <h3 class="abs foot-head" style="left:821px">Contact Us</h3>
  <div class="abs contact-row" style="top:3496px"><svg width="13" height="13" viewBox="0 0 13 13" fill="#f04b4f"><path d="M3 1l2 3-1.5 1.5a8 8 0 0 0 4 4L9 8l3 2-1 2.5C5 12 1 8 .5 2z"/></svg>Phone: 000-000-0000</div>
  <div class="abs contact-row" style="top:3528px"><svg width="13" height="11" viewBox="0 0 13 11" fill="#f04b4f"><rect width="13" height="11" rx="1"/><path d="M1 1.5l5.5 4 5.5-4" stroke="#fff" fill="none"/></svg>Email: hello@velmorocrafts.com</div>
  <a class="abs social" style="left:822px" href="#" aria-label="Social profile"><i></i></a>
  <a class="abs social" style="left:870px" href="#" aria-label="Social profile"><i></i></a>
  <div class="abs rule"></div>
  <p class="abs copyright">© 2025 All Rights Reserved.</p>
  <a class="abs totop" href="#" aria-label="Back to top"><svg width="12" height="12" viewBox="0 0 12 12"><path d="M3 7.5 6 4.5l3 3" fill="none" stroke="#fff" stroke-width="1.6"/></svg></a>
</footer>

</body>
</html>
```